Business Card Design Project

I would like to have a project of business card with incorporated attachted logo elements in warm colors like: gold, yellow, brown.
We would like incorporate below information into the design
Name of the Company: Continental Hoop Invitational
Name: Dorian Pelkey
Position: Project Director
e-mail: dorian@hoopinvitational.net
mobile: +65 83147092
website: www.hoopinvitational.net
Address: 47 Marbury Lane, #06-11, Singapore 915274
There is a picture attachted which can be used as a back side of the buisness card - we would like to follow the colors theme on the front card ( with the person contact details) how ever the front card we will prefer with white background but with graphfic elements coming from logo.
Project Deadline Extended
Reason: the project has been launched on 24 of April with deadline by 24 of April by mistakes. Thats why I would like to extend the deadline.
Name: Dorian Pelkey
mobile: +65 83147092

```html
<!DOCTYPE html>
<html lang="en">
<head>
<meta charset="utf-8">
<title>Continental Hoop Invitational – Business Card, Side A</title>
<link rel="stylesheet" href="https://fonts.googleapis.com/css2?family=Open+Sans:wght@600&family=Arimo:wght@400&family=Carlito:wght@400&display=swap">
<style>
  :root {
    --page: #ffffff;
    --card: #ffffff;
    --card-edge: #3a3a3a;
    --brand-red: #e8232a;
    --ink: #111111;
    --flame-yellow: #fde81e;
    --flame-orange: #f7931e;
    --flame-red: #e5261f;
  }
  html, body {
    margin: 0;
    padding: 0;
    width: 1200px;
    height: 1200px;
    overflow: hidden;
    background: var(--page);
  }
  .canvas {
    position: relative;
    width: 1200px;
    height: 1200px;
  }
  .card {
    position: absolute;
    left: 50px;
    top: 203px;
    width: 1099px;
    height: 670px;
    background: var(--card);
    border: 1.5px solid var(--card-edge);
    overflow: hidden;
  }
  .brand-graphic {
    position: absolute;
    right: 0;
    top: 0;
    width: 400px;
    height: 100%;
  }
  .company {
    position: absolute;
    left: 34px;
    top: 42px;
    margin: 0;
    font-family: "Open Sans", sans-serif;
    font-weight: 600;
    color: var(--brand-red);
    text-transform: uppercase;
    line-height: 1;
  }
  .company-line1 {
    display: block;
    font-size: 42px;
    letter-spacing: 1.2px;
  }
  .company-line2 {
    display: block;
    font-size: 62px;
    letter-spacing: 1px;
    margin-top: 8px;
  }
  .person, .contact, .website {
    position: absolute;
    left: 22px;
    margin: 0;
    font-family: "Arimo", sans-serif;
    font-weight: 400;
    line-height: 1;
  }
  .person { top: 259px; }
  .person-name {
    display: block;
    font-size: 45px;
    color: var(--ink);
  }
  .person-role {
    display: block;
    font-size: 33px;
    color: var(--brand-red);
    margin-top: 14px;
  }
  .contact {
    top: 425px;
    font-style: normal;
    font-size: 28px;
    color: var(--ink);
  }
  .contact span {
    display: block;
    height: 40.5px;
  }
  .website {
    top: 591px;
    font-size: 28px;
    color: var(--brand-red);
  }
  .side-label {
    position: absolute;
    left: 0;
    width: 1200px;
    top: 990px;
    margin: 0;
    text-align: center;
    font-family: "Carlito", sans-serif;
    font-size: 51px;
    line-height: 1;
    color: #000;
  }
</style>
</head>
<body>
<main class="canvas">
  <section class="card">
    <svg class="brand-graphic" viewBox="0 0 400 670" role="img" aria-label="Brand symbol area in warm yellow, orange and red tones">
      <defs>
        <linearGradient id="flame" x1="0" y1="1" x2="1" y2="0">
          <stop offset="0" stop-color="var(--flame-yellow)" style="stop-color:#fde81e"/>
          <stop offset="0.45" stop-color="#f7931e"/>
          <stop offset="1" stop-color="#e5261f"/>
        </linearGradient>
      </defs>
      <rect x="0" y="0" width="400" height="670" fill="url(#flame)" opacity="0.85"/>
    </svg>

    <h1 class="company">
      <span class="company-line1">Continental Hoop</span>
      <span class="company-line2">Invitational</span>
    </h1>

    <p class="person">
      <span class="person-name">Dorian Pelkey</span>
      <span class="person-role">Project Director</span>
    </p>

    <address class="contact">
      <span>47 Marbury Lane, #06-11, Singapore 915274</span>
      <span>dorian@hoopinvitational.net</span>
      <span>+65 83147092</span>
    </address>

    <p class="website">www.hoopinvitational.net</p>
  </section>

  <p class="side-label">Side A</p>
</main>
</body>
</html>
```